Eye catching unique, memorable and recognizable Label for bottled water needed

Looking for a water label that can be branded and recognized just by the colors from across a tennis court. Looking for high contrast or colorful. Can be bright and colorful or just black. The label needs to fit two sizes of bottles. Label sizes are 5"x8" and 3.75"x 7". We need the logo to be on the label. Looking for bright eye catching fun label. I am attaching our current smoothie cup as possible inspo as well. Also, hide the words "Be Kind Be Happy Be Healthy" We have those words in a lighter shade of yellow on our smoothie cup, almost invisible. would be neat to hide it design somehow.
There are not any designs our franchise team has liked enough to move forward

```html
<!DOCTYPE html>
<html lang="en">
<head>
<meta charset="utf-8">
<title>Fresh Point Nutrition – Bottle Labels</title>
<link href="https://fonts.googleapis.com/css2?family=Montserrat:wght@400;600;700;800&family=Oswald:wght@400;500&display=swap" rel="stylesheet">
<style>
  :root {
    --canvas-bg: #e9e9e9;
    --ink: #1f1f1f;
    --white: #ffffff;
    --facts-bg: #ffffff;
    --accent-red: #e3262b;
    --info-navy: #1c3f8c;
    --green-a: #b4e35f; --green-b: #2ea24a; --green-c: #0a8a3c; --green-d: #8fd160;
    --red-a: #ffb62c;   --red-b: #ff3a16;   --red-c: #f2000f;   --red-d: #ff8c1c;
    --blue-a: #93d27a;  --blue-b: #2f7fc0;  --blue-c: #0a4aa0;  --blue-d: #6fb3bd;
    --yellow-a: #fff06a;--yellow-b: #ffdc10;--yellow-c: #ffcc00;--yellow-d: #ffe655;
  }
  * { box-sizing: border-box; margin: 0; padding: 0; }
  html, body { width: 1004px; height: 1200px; overflow: hidden; }
  body {
    background: radial-gradient(ellipse at 50% 55%, #f7f7f7 0%, var(--canvas-bg) 70%);
    font-family: "Montserrat", sans-serif;
    position: relative;
  }
  .label {
    position: absolute;
    width: 443px;
    height: 277px;
    overflow: hidden;
    color: var(--white);
  }
  .label--green  { left: 40px;  top: 32px;  background: linear-gradient(135deg, var(--green-a) 0%, var(--green-b) 38%, var(--green-c) 55%, var(--green-d) 100%); }
  .label--red    { left: 520px; top: 32px;  background: linear-gradient(135deg, var(--red-a) 0%, var(--red-b) 38%, var(--red-c) 55%, var(--red-d) 100%); }
  .label--blue   { left: 40px;  top: 359px; background: linear-gradient(135deg, var(--blue-a) 0%, var(--blue-b) 38%, var(--blue-c) 55%, var(--blue-d) 100%); }
  .label--yellow { left: 520px; top: 359px; background: linear-gradient(135deg, var(--yellow-a) 0%, var(--yellow-b) 38%, var(--yellow-c) 55%, var(--yellow-d) 100%); }

  .label__shapes { position: absolute; inset: 0; }

  .label__warning {
    position: absolute;
    left: 32px; top: 30px;
    height: 218px;
    writing-mode: vertical-rl;
    transform: rotate(180deg);
    font-family: "Oswald", sans-serif;
    font-size: 5.6px;
    line-height: 1.35;
    color: rgba(25, 25, 25, 0.85);
    width: 34px;
  }
  .label__warning strong { font-weight: 500; }

  .brand {
    position: absolute;
    left: 128px; top: 100px;
    display: flex; align-items: center; gap: 6px;
  }
  .brand__dot { width: 14px; height: 14px; border-radius: 50%; background: var(--accent-red); flex: none; }
  .brand__name {
    font-weight: 800;
    font-size: 21px;
    line-height: 1.05;
    color: var(--ink);
  }

  .label__volume {
    position: absolute;
    left: 180px; top: 226px;
    width: 84px;
    text-align: center;
    font-weight: 700;
    line-height: 1;
  }
  .label__abv { font-size: 9px; }
  .label__abv-unit { font-size: 3.2px; font-weight: 600; display: block; margin-top: 1px; }
  .label__size { font-size: 5.6px; font-weight: 600; display: block; margin-top: 5px; }

  .label__claims {
    position: absolute;
    left: 345px; top: 70px;
    width: 84px;
    font-size: 2.9px;
    font-weight: 700;
    line-height: 1.6;
    color: var(--info-navy);
  }

  .facts {
    position: absolute;
    left: 346px; top: 87px;
    width: 81px;
    background: var(--facts-bg);
    border: 0.8px solid var(--ink);
    padding: 1.5px 2px 2px;
    color: var(--ink);
    font-family: "Montserrat", sans-serif;
  }
  .facts__title { font-size: 8.6px; font-weight: 800; line-height: 1; border-bottom: 0.6px solid var(--ink); padding-bottom: 1px; }
  .facts__line { font-size: 4.6px; line-height: 1.35; display: flex; justify-content: space-between; }
  .facts__line--bold { font-weight: 800; }
  .facts__line--indent { padding-left: 5px; }
  .facts__tiny { font-size: 2.6px; font-weight: 700; margin-top: 1px; }
  .facts__cal { font-size: 9.5px; font-weight: 800; line-height: 1; display: flex; justify-content: space-between; }
  .facts__bar { height: 2.6px; background: var(--ink); margin: 1.5px 0; }
  .facts__rule { height: 0.5px; background: var(--ink); margin: 0.5px 0; }
  .facts__mini { font-size: 3.3px; line-height: 1.8; display: flex; justify-content: space-between; }

  .label__ingredients {
    position: absolute;
    left: 346px; top: 213px;
    width: 84px;
    font-size: 3.5px;
    line-height: 1.45;
    font-weight: 400;
    color: rgba(255, 255, 255, 0.85);
  }
  .label__producer {
    position: absolute;
    left: 346px; top: 239px;
    width: 86px;
    font-size: 3.4px;
    line-height: 1.45;
    font-weight: 700;
    color: rgba(255, 255, 255, 0.92);
  }
</style>
</head>
<body>

<!-- Green -->
<section class="label label--green">
  <svg class="label__shapes" width="443" height="277" viewBox="0 0 443 277" aria-hidden="true">
    <path d="M0 20 C80 0 160 40 260 10 L443 0 L443 0 L0 0 Z" fill="rgba(255,255,255,0.12)"/>
    <path d="M0 250 C120 210 260 260 443 215 L443 277 L0 277 Z" fill="rgba(255,255,255,0.12)"/>
    <circle cx="277" cy="4" r="52" fill="none" stroke="#fff" stroke-width="1.2"/>
    <circle cx="103" cy="295" r="55" fill="none" stroke="#fff" stroke-width="1.2"/>
    <circle cx="169" cy="214" r="18" fill="none" stroke="rgba(255,255,255,0.35)" stroke-width="2"/>
    <circle cx="176" cy="37" r="5" fill="#d8f25a"/>
    <circle cx="304" cy="123" r="6" fill="#d8f25a"/>
  </svg>
  <p class="label__warning"><strong>GOVERNMENT WARNING:</strong> (1) According to the Surgeon General, women should not drink alcoholic beverages during pregnancy because of the risk of birth defects. (2) Consumption of alcoholic beverages impairs your ability to drive a car or operate machinery, and may cause health problems.</p>
  <div class="brand"><span class="brand__dot"></span><span class="brand__name">Fresh Point<br>Nutrition</span></div>
  <div class="label__volume"><span class="label__abv">5%</span><span class="label__abv-unit">ALC/VOL</span><span class="label__size">12 OZ (355ml)</span></div>
  <p class="label__claims">80 CALORIES · NO ADDED SUGAR · 3G CARBS<br>CONTAINS ALCOHOL · CONTAINS REAL JUICE</p>
  <div class="facts">
    <div class="facts__title">Nutrition Facts</div>
    <div class="facts__line">1 serving per can</div>
    <div class="facts__line facts__line--bold"><span>Serving size</span><span>12 OZ (340g)</span></div>
    <div class="facts__bar"></div>
    <div class="facts__tiny">Amount per serving</div>
    <div class="facts__cal"><span>Calories</span><span>100</span></div>
    <div class="facts__bar"></div>
    <div class="facts__line facts__line--bold"><span>Total Fat</span><span>0g</span></div>
    <div class="facts__line facts__line--bold"><span>Sodium</span><span>4mg</span></div>
    <div class="facts__line facts__line--bold"><span>Net Carbohydrates</span><span>3g</span></div>
    <div class="facts__line facts__line--indent"><span>Total Sugars 3g</span></div>
    <div class="facts__line facts__line--bold"><span>Protein</span><span>0g</span></div>
    <div class="facts__bar"></div>
    <div class="facts__mini"><span>Vitamin D 0mg</span><span>Calcium 8.9mg</span></div>
    <div class="facts__mini"><span>Iron &lt;0.176mg</span><span>Potassium 29.3mg</span></div>
  </div>
  <p class="label__ingredients">INGREDIENTS:<br>FILTERED WATER, PREMIUM CORN BASE VODKA, BLACK TEA, LEMON JUICE, MONK FRUIT.</p>
  <p class="label__producer">PRODUCED &amp; DISTRIBUTED BY:<br>LUMEN SPIRITS COMPANY, LLC IN<br>MILFORD, OH</p>
</section>

<!-- Red -->
<section class="label label--red">
  <svg class="label__shapes" width="443" height="277" viewBox="0 0 443 277" aria-hidden="true">
    <path d="M0 20 C80 0 160 40 260 10 L443 0 L0 0 Z" fill="rgba(255,255,255,0.12)"/>
    <path d="M0 250 C120 210 260 260 443 215 L443 277 L0 277 Z" fill="rgba(255,255,255,0.12)"/>
    <circle cx="277" cy="4" r="52" fill="none" stroke="#fff" stroke-width="1.2"/>
    <circle cx="103" cy="295" r="55" fill="none" stroke="#fff" stroke-width="1.2"/>
    <circle cx="169" cy="214" r="18" fill="none" stroke="rgba(255,255,255,0.35)" stroke-width="2"/>
    <circle cx="176" cy="37" r="5" fill="#d8f25a"/>
    <circle cx="304" cy="123" r="6" fill="#d8f25a"/>
  </svg>
  <p class="label__warning"><strong>GOVERNMENT WARNING:</strong> (1) According to the Surgeon General, women should not drink alcoholic beverages during pregnancy because of the risk of birth defects. (2) Consumption of alcoholic beverages impairs your ability to drive a car or operate machinery, and may cause health problems.</p>
  <div class="brand"><span class="brand__dot"></span><span class="brand__name">Fresh Point<br>Nutrition</span></div>
  <div class="label__volume"><span class="label__abv">5%</span><span class="label__abv-unit">ALC/VOL</span><span class="label__size">12 OZ (355ml)</span></div>
  <p class="label__claims">80 CALORIES · NO ADDED SUGAR · 3G CARBS<br>CONTAINS ALCOHOL · CONTAINS REAL JUICE</p>
  <div class="facts">
    <div class="facts__title">Nutrition Facts</div>
    <div class="facts__line">1 serving per can</div>
    <div class="facts__line facts__line--bold"><span>Serving size</span><span>12 OZ (340g)</span></div>
    <div class="facts__bar"></div>
    <div class="facts__tiny">Amount per serving</div>
    <div class="facts__cal"><span>Calories</span><span>100</span></div>
    <div class="facts__bar"></div>
    <div class="facts__line facts__line--bold"><span>Total Fat</span><span>0g</span></div>
    <div class="facts__line facts__line--bold"><span>Sodium</span><span>4mg</span></div>
    <div class="facts__line facts__line--bold"><span>Net Carbohydrates</span><span>3g</span></div>
    <div class="facts__line facts__line--indent"><span>Total Sugars 3g</span></div>
    <div class="facts__line facts__line--bold"><span>Protein</span><span>0g</span></div>
    <div class="facts__bar"></div>
    <div class="facts__mini"><span>Vitamin D 0mg</span><span>Calcium 8.9mg</span></div>
    <div class="facts__mini"><span>Iron &lt;0.176mg</span><span>Potassium 29.3mg</span></div>
  </div>
  <p class="label__ingredients">INGREDIENTS:<br>FILTERED WATER, PREMIUM CORN BASE VODKA, BLACK TEA, LEMON JUICE, MONK FRUIT.</p>
  <p class="label__producer">PRODUCED &amp; DISTRIBUTED BY:<br>LUMEN SPIRITS COMPANY, LLC IN<br>MILFORD, OH</p>
</section>

<!-- Blue -->
<section class="label label--blue">
  <svg class="label__shapes" width="443" height="277" viewBox="0 0 443 277" aria-hidden="true">
    <path d="M0 20 C80 0 160 40 260 10 L443 0 L0 0 Z" fill="rgba(255,255,255,0.12)"/>
    <path d="M0 250 C120 210 260 260 443 215 L443 277 L0 277 Z" fill="rgba(255,255,255,0.12)"/>
    <circle cx="277" cy="4" r="52" fill="none" stroke="#fff" stroke-width="1.2"/>
    <circle cx="103" cy="295" r="55" fill="none" stroke="#fff" stroke-width="1.2"/>
    <circle cx="169" cy="214" r="18" fill="none" stroke="rgba(60,140,230,0.6)" stroke-width="2"/>
    <circle cx="176" cy="37" r="5" fill="#d8f25a"/>
    <circle cx="304" cy="123" r="6" fill="#d8f25a"/>
  </svg>
  <p class="label__warning"><strong>GOVERNMENT WARNING:</strong> (1) According to the Surgeon General, women should not drink alcoholic beverages during pregnancy because of the risk of birth defects. (2) Consumption of alcoholic beverages impairs your ability to drive a car or operate machinery, and may cause health problems.</p>
  <div class="brand"><span class="brand__dot"></span><span class="brand__name">Fresh Point<br>Nutrition</span></div>
  <div class="label__volume"><span class="label__abv">5%</span><span class="label__abv-unit">ALC/VOL</span><span class="label__size">12 OZ (355ml)</span></div>
  <p class="label__claims">80 CALORIES · NO ADDED SUGAR · 3G CARBS<br>CONTAINS ALCOHOL · CONTAINS REAL JUICE</p>
  <div class="facts">
    <div class="facts__title">Nutrition Facts</div>
    <div class="facts__line">1 serving per can</div>
    <div class="facts__line facts__line--bold"><span>Serving size</span><span>12 OZ (340g)</span></div>
    <div class="facts__bar"></div>
    <div class="facts__tiny">Amount per serving</div>
    <div class="facts__cal"><span>Calories</span><span>100</span></div>
    <div class="facts__bar"></div>
    <div class="facts__line facts__line--bold"><span>Total Fat</span><span>0g</span></div>
    <div class="facts__line facts__line--bold"><span>Sodium</span><span>4mg</span></div>
    <div class="facts__line facts__line--bold"><span>Net Carbohydrates</span><span>3g</span></div>
    <div class="facts__line facts__line--indent"><span>Total Sugars 3g</span></div>
    <div class="facts__line facts__line--bold"><span>Protein</span><span>0g</span></div>
    <div class="facts__bar"></div>
    <div class="facts__mini"><span>Vitamin D 0mg</span><span>Calcium 8.9mg</span></div>
    <div class="facts__mini"><span>Iron &lt;0.176mg</span><span>Potassium 29.3mg</span></div>
  </div>
  <p class="label__ingredients">INGREDIENTS:<br>FILTERED WATER, PREMIUM CORN BASE VODKA, BLACK TEA, LEMON JUICE, MONK FRUIT.</p>
  <p class="label__producer">PRODUCED &amp; DISTRIBUTED BY:<br>LUMEN SPIRITS COMPANY, LLC IN<br>MILFORD, OH</p>
</section>

<!-- Yellow -->
<section class="label label--yellow">
  <svg class="label__shapes" width="443" height="277" viewBox="0 0 443 277" aria-hidden="true">
    <path d="M0 20 C80 0 160 40 260 10 L443 0 L0 0 Z" fill="rgba(255,255,255,0.15)"/>
    <path d="M0 250 C120 210 260 260 443 215 L443 277 L0 277 Z" fill="rgba(255,255,255,0.15)"/>
    <circle cx="277" cy="4" r="52" fill="none" stroke="#fff" stroke-width="1.2"/>
    <circle cx="103" cy="295" r="55" fill="none" stroke="#fff" stroke-width="1.2"/>
    <circle cx="169" cy="214" r="18" fill="none" stroke="rgba(255,255,255,0.5)" stroke-width="2"/>
    <circle cx="176" cy="37" r="5" fill="#b8ec6a"/>
    <circle cx="304" cy="123" r="6" fill="#b8ec6a"/>
  </svg>
  <p class="label__warning"><strong>GOVERNMENT WARNING:</strong> (1) According to the Surgeon General, women should not drink alcoholic beverages during pregnancy because of the risk of birth defects. (2) Consumption of alcoholic beverages impairs your ability to drive a car or operate machinery, and may cause health problems.</p>
  <div class="brand"><span class="brand__dot"></span><span class="brand__name">Fresh Point<br>Nutrition</span></div>
  <div class="label__volume"><span class="label__abv">5%</span><span class="label__abv-unit">ALC/VOL</span><span class="label__size">12 OZ (355ml)</span></div>
  <p class="label__claims">80 CALORIES · NO ADDED SUGAR · 3G CARBS<br>CONTAINS ALCOHOL · CONTAINS REAL JUICE</p>
  <div class="facts">
    <div class="facts__title">Nutrition Facts</div>
    <div class="facts__line">1 serving per can</div>
    <div class="facts__line facts__line--bold"><span>Serving size</span><span>12 OZ (340g)</span></div>
    <div class="facts__bar"></div>
    <div class="facts__tiny">Amount per serving</div>
    <div class="facts__cal"><span>Calories</span><span>100</span></div>
    <div class="facts__bar"></div>
    <div class="facts__line facts__line--bold"><span>Total Fat</span><span>0g</span></div>
    <div class="facts__line facts__line--bold"><span>Sodium</span><span>4mg</span></div>
    <div class="facts__line facts__line--bold"><span>Net Carbohydrates</span><span>3g</span></div>
    <div class="facts__line facts__line--indent"><span>Total Sugars 3g</span></div>
    <div class="facts__line facts__line--bold"><span>Protein</span><span>0g</span></div>
    <div class="facts__bar"></div>
    <div class="facts__mini"><span>Vitamin D 0mg</span><span>Calcium 8.9mg</span></div>
    <div class="facts__mini"><span>Iron &lt;0.176mg</span><span>Potassium 29.3mg</span></div>
  </div>
  <p class="label__ingredients">INGREDIENTS:<br>FILTERED WATER, PREMIUM CORN BASE VODKA, BLACK TEA, LEMON JUICE, MONK FRUIT.</p>
  <p class="label__producer">PRODUCED &amp; DISTRIBUTED BY:<br>LUMEN SPIRITS COMPANY, LLC IN<br>MILFORD, OH</p>
</section>

</body>
</html>
```